4th Generation Family Business Needs a New Card Design!

We are a family owned 4th Generation company. We are based in the Sydney, Australia area and we are desperately in need of a more modern and classy card. We are monumental masons who design, supply & erect lasting memorials throughout cemeteries in Sydney. Our customers are normally in a period of grieving. I have attached logo files that will need to be implemented on the card. Company was established 1935. Australian Owned and Operated. Card needs to be designed to PRINTLY.com specification.

Target Market(s)

Our target market is based upon people that a grieving for family members that have passed away. We also deal with alot of companies that own and operate cemeteries.

Industry/Entity Type

Business

Contact Information for Business Card

Oliver Brantley, Operations Manager, 0417552908, oliver@hollowaystoneworks.com.au
Martin Brantley, Director, 0431906627, martin@hollowaystoneworks.com.au
Phone # 02 9634 2258
Website: www.hollowaystoneworks.com.au
Address: Suite 17, 8 Calloway Lane, East Penrose, Sydney NSW 2290

Font styles to use
Serif
Decorative
Script

Requirements
Must have
• Would like to see the logo nicely implemented with a modern design. Embossed lettering would be a nice additive.

```html
<!DOCTYPE html>
<html lang="en">
<head>
<meta charset="utf-8">
<title>Holloway Stoneworks – Business Card</title>
<link rel="stylesheet" href="https://fonts.googleapis.com/css2?family=Cinzel:wght@500&family=Lato:wght@400;700&display=swap">
<style>
  :root {
    --backdrop: #e7e4df;
    --card-white: #ffffff;
    --charcoal: #222222;
    --charcoal-soft: #2a2a2a;
    --gold: #e8b923;
    --grey-text: #8a8a8a;
    --grey-rule: #cfcfcf;
    --light-text: #f2f2f2;
  }
  * { margin: 0; padding: 0; box-sizing: border-box; }
  html, body { width: 1200px; height: 960px; overflow: hidden; }
  body {
    background: var(--backdrop);
    font-family: "Lato", sans-serif;
    position: relative;
  }
  .card {
    position: absolute;
    left: 220px;
    width: 760px;
    height: 434px;
    box-shadow: 0 4px 14px rgba(0,0,0,0.18);
    overflow: hidden;
  }
  .card--front { top: 30px; background: var(--card-white); }
  .card--back {
    top: 496px;
    background: radial-gradient(circle at 50% 40%, var(--charcoal-soft), var(--charcoal));
  }

  /* brand name lockup */
  .brand {
    position: absolute;
    left: 0; right: 0;
    display: flex;
    justify-content: center;
    align-items: center;
    gap: 14px;
    font-family: "Cinzel", serif;
    font-weight: 500;
    letter-spacing: 1px;
  }
  .brand__mark { width: 18px; height: 18px; }
  .card--front .brand { top: 120px; font-size: 40px; color: var(--charcoal); }
  .card--front .brand__mark { background: var(--gold); }
  .card--back .brand { top: 220px; font-size: 46px; color: var(--light-text); }
  .card--back .brand__mark { background: var(--gold); }

  /* people */
  .people {
    position: absolute;
    top: 230px;
    left: 0; right: 0;
    height: 112px;
  }
  .people__divider {
    position: absolute;
    left: 380px; top: 4px;
    width: 1px; height: 106px;
    background: var(--grey-rule);
  }
  .person { position: absolute; top: 0; width: 370px; }
  .person--left { right: 398px; text-align: right; top: 4px; }
  .person--right { left: 396px; text-align: left; }
  .person__name {
    color: var(--gold);
    font-weight: 700;
    font-size: 25px;
    letter-spacing: 0.6px;
    line-height: 1.1;
  }
  .person__role {
    color: var(--grey-text);
    font-size: 19px;
    letter-spacing: 1px;
    margin-top: 2px;
    margin-bottom: 10px;
  }
  .person__line {
    display: flex;
    align-items: center;
    gap: 10px;
    color: var(--grey-text);
    font-size: 17px;
    line-height: 25px;
  }
  .person--left .person__line { justify-content: flex-end; }
  .icon { width: 14px; height: 14px; flex: none; }

  /* company band */
  .company-band {
    position: absolute;
    left: 0; right: 0; bottom: 0;
    height: 72px;
    background: var(--charcoal);
    border-top: 4px solid var(--gold);
    color: var(--light-text);
    text-align: center;
    font-size: 17px;
    padding-top: 10px;
    line-height: 25px;
  }
  .company-band__label { color: var(--gold); font-weight: 700; }
  .company-band__contact {
    display: flex; justify-content: center; align-items: center; gap: 6px;
  }
  .company-band__contact .icon { width: 14px; height: 14px; }
  .company-band__gap { width: 6px; }

  .back-web {
    position: absolute;
    top: 352px; left: 0; right: 0;
    text-align: center;
    color: var(--light-text);
    font-size: 17px;
    letter-spacing: 4px;
  }
  .back-web__domain { color: var(--gold); }
</style>
</head>
<body>

<section class="card card--front">
  <div class="brand"><span class="brand__mark"></span>Holloway Stoneworks</div>

  <div class="people">
    <div class="person person--left">
      <div class="person__name">Martin Brantley</div>
      <div class="person__role">Director</div>
      <div class="person__line">0431906627
        <svg class="icon" viewBox="0 0 14 14"><rect x="3.5" y="0.8" width="7" height="12.4" rx="1.2" fill="none" stroke="#e8b923" stroke-width="1.4"/><line x1="6" y1="11" x2="8" y2="11" stroke="#e8b923" stroke-width="1.2"/></svg>
      </div>
      <div class="person__line">martin@hollowaystoneworks.com.au
        <svg class="icon" viewBox="0 0 14 14"><rect x="0.8" y="2.8" width="12.4" height="8.4" fill="none" stroke="#e8b923" stroke-width="1.4"/><polyline points="1,3 7,8 13,3" fill="none" stroke="#e8b923" stroke-width="1.2"/></svg>
      </div>
    </div>
    <div class="people__divider"></div>
    <div class="person person--right">
      <div class="person__name">Oliver Brantley</div>
      <div class="person__role">Operations Manager</div>
      <div class="person__line">
        <svg class="icon" viewBox="0 0 14 14"><rect x="3.5" y="0.8" width="7" height="12.4" rx="1.2" fill="none" stroke="#e8b923" stroke-width="1.4"/><line x1="6" y1="11" x2="8" y2="11" stroke="#e8b923" stroke-width="1.2"/></svg>
        0417552908</div>
      <div class="person__line">
        <svg class="icon" viewBox="0 0 14 14"><rect x="0.8" y="2.8" width="12.4" height="8.4" fill="none" stroke="#e8b923" stroke-width="1.4"/><polyline points="1,3 7,8 13,3" fill="none" stroke="#e8b923" stroke-width="1.2"/></svg>
        oliver@hollowaystoneworks.com.au</div>
    </div>
  </div>

  <footer class="company-band">
    <div><span class="company-band__label">Holloway Stoneworks:</span> Suite 17, 8 Calloway Lane, East Penrose, Sydney NSW 2290</div>
    <div class="company-band__contact">
      <svg class="icon" viewBox="0 0 14 14"><path d="M4 1 L6 4 L4.5 5.5 C5.5 8 6.5 9 8.5 9.8 L10 8.3 L13 10.3 L11.5 13 C6 12.5 1.5 8 1 2.5 Z" fill="#e8b923"/></svg>
      02 9634 2258
      <span class="company-band__gap"></span>
      <svg class="icon" viewBox="0 0 14 14"><circle cx="7" cy="7" r="6" fill="none" stroke="#e8b923" stroke-width="1.3"/><ellipse cx="7" cy="7" rx="2.6" ry="6" fill="none" stroke="#e8b923" stroke-width="1.1"/><line x1="1" y1="7" x2="13" y2="7" stroke="#e8b923" stroke-width="1.1"/></svg>
      www.hollowaystoneworks.com.au
    </div>
  </footer>
</section>

<section class="card card--back">
  <div class="brand"><span class="brand__mark"></span>Holloway Stoneworks</div>
  <div class="back-web">www.<span class="back-web__domain">hollowaystoneworks</span>.com.au</div>
</section>

</body>
</html>
```